Copper Lantern: A Self Care Session for Employees

I need a flyer for organizations and businnesses. I am offering a session that will address behavioral issues such as coming to work late, not getting along with others and not working together as a team. I am a life coach who works with difficult employees, helping them address their issues and helping them be a better version of themselves. I also offer a leadership class for managers. I would like the flyer to be professional, clean and convey a feeling of trust. I would prefer to see disgns that use the color blue.

Target Market(s)

small businesses

Industry/Entity Type

Work

Font styles to use
Sans Serif

Colors
34a7d8
85cae6
0792cd
ffffff

Requirements
Must have
• shades of blue and perhaps white. should be clean, fresh and professional
Nice to have
• simple yet warm
Should not have
• distracting and heavy, playful

```html
<!DOCTYPE html>
<html lang="en">
<head>
<meta charset="utf-8">
<title>Copper Lantern – A Self Care Session for Employees</title>
<link rel="stylesheet" href="https://fonts.googleapis.com/css2?family=Roboto+Condensed:wght@400;700&family=Open+Sans:wght@400;600&display=swap">
<style>
  :root {
    --blue: #0792cd;
    --blue-mid: #34a7d8;
    --blue-light: #85cae6;
    --white: #ffffff;
    --grey-band: #58595b;
    --grey-text: #5f6062;
    --ink: #111111;
    --backdrop: #d9dcdf;
    --photo-dark: #0d1a2a;
    --photo-light: #6f93b8;
  }
  * { margin: 0; padding: 0; box-sizing: border-box; }
  html, body { width: 707px; height: 1200px; overflow: hidden; background: var(--backdrop); }
  .flyer {
    position: absolute; left: 0; top: 100px;
    width: 707px; height: 1000px;
    background: var(--white);
    font-family: "Roboto Condensed", Arial, sans-serif;
    overflow: hidden;
  }
  .hero { position: absolute; left: 0; top: 0; width: 707px; height: 570px; }
  .brand {
    position: absolute; left: 430px; top: 430px; width: 260px;
    display: flex; align-items: center; gap: 10px;
    font-weight: 700; font-size: 26px; color: var(--grey-text); line-height: 1;
  }
  .brand-mark { width: 18px; height: 18px; background: var(--blue-mid); flex: none; }
  .kicker {
    position: absolute; top: 586px; width: 100%; text-align: center;
    color: var(--blue); font-size: 21px; letter-spacing: 0.5px;
  }
  .headline {
    position: absolute; top: 613px; width: 100%; text-align: center;
    color: var(--grey-text); font-size: 30px; font-weight: 700;
  }
  .band {
    position: absolute; left: 0; width: 100%; text-align: center;
    color: var(--white); font-weight: 700; font-size: 23px;
    display: flex; align-items: center; justify-content: center;
  }
  .band-blue { top: 663px; height: 55px; background: var(--blue); }
  .band-grey { top: 734px; height: 57px; background: var(--grey-band); }
  .coach-card {
    position: absolute; left: 107px; top: 816px; width: 500px; height: 120px;
  }
  .coach-portrait {
    position: absolute; left: 0; top: 5px; width: 76px; height: 110px;
    background: linear-gradient(160deg, #c9b7a6, #5a4436 70%, #2b3f63);
  }
  .coach-note {
    position: absolute; left: 82px; top: 0; width: 412px; height: 120px;
    border: 1px solid #d6d6d6; padding: 12px 0 0 40px;
    color: var(--grey-text); font-size: 18px; line-height: 25px;
  }
  .coach-cta {
    color: var(--blue); font-size: 46px; font-weight: 700; line-height: 48px; letter-spacing: 1px;
  }
  .footer { position: absolute; left: 0; top: 952px; width: 707px; height: 48px; }
  .footer-contact {
    position: absolute; left: 56px; top: 962px;
    font-family: "Open Sans", Arial, sans-serif; font-size: 13px; color: var(--white);
  }
  .footer-contact span { color: var(--blue-light); }
  .footer-phone {
    position: absolute; left: 400px; top: 958px;
    display: flex; align-items: center; gap: 8px;
    color: var(--white); font-weight: 700; font-size: 24px;
  }
  .footer-phone .divider { margin: 0 4px; font-weight: 400; }
</style>
</head>
<body>
<main class="flyer">
  <svg class="hero" viewBox="0 0 707 570" xmlns="http://www.w3.org/2000/svg">
    <defs>
      <linearGradient id="officeTone" x1="0" y1="0" x2="1" y2="1">
        <stop offset="0" stop-color="var(--photo-light)"/>
        <stop offset="0.55" stop-color="#2c4563"/>
        <stop offset="1" stop-color="var(--photo-dark)"/>
      </linearGradient>
    </defs>
    <path role="img" aria-label="Photo of a stressed office worker with head in hands at a desk by a window"
          fill="url(#officeTone)"
          d="M0 0 H707 V154 L196 530 Q146 566 100 530 L0 445 Z"/>
    <path fill="var(--blue-mid)" d="M707 112 V154 L520 292 L500 280 Z"/>
    <rect x="612" y="280" width="30" height="30" rx="6" fill="var(--blue-mid)"/>
    <rect x="628" y="294" width="30" height="30" rx="6" fill="var(--blue-light)"/>
  </svg>

  <div class="brand"><span class="brand-mark"></span>Harbor Path Coaching</div>

  <p class="kicker">COPPER LANTERN:</p>
  <h1 class="headline">A SELF CARE SESSION FOR EMPLOYEES</h1>

  <div class="band band-blue">Are Your Employees Bringing Personal Issues On The Job?</div>
  <div class="band band-grey">Is It Affecting Team Communication Or May Be Even Productivity?</div>

  <section class="coach-card">
    <div class="coach-portrait" role="img" aria-label="Portrait photo of the coach"></div>
    <div class="coach-note">
      IF THE BEHAVIOR OF AN EMPLOYEE, MANAGER OR<br>
      YOUR ENTIRE STAFF IS A PROBLEM
      <div class="coach-cta">I CAN HELP</div>
    </div>
  </section>

  <svg class="footer" viewBox="0 0 707 48" xmlns="http://www.w3.org/2000/svg">
    <path fill="var(--ink)" d="M0 0 H372 L352 30 H0 Z"/>
    <path fill="var(--blue)" d="M380 0 H707 V40 H354 Z"/>
    <rect x="0" y="40" width="707" height="8" fill="var(--blue)"/>
  </svg>
  <p class="footer-contact">For more information contact <span>Dana Morrow</span></p>
  <div class="footer-phone">
    <svg width="20" height="20" viewBox="0 0 24 24" aria-hidden="true">
      <path fill="var(--white)" d="M6.6 10.8a15.1 15.1 0 0 0 6.6 6.6l2.2-2.2c.3-.3.7-.4 1-.2 1.1.4 2.3.6 3.6.6.6 0 1 .4 1 1V20c0 .6-.4 1-1 1A17 17 0 0 1 3 4c0-.6.4-1 1-1h3.5c.6 0 1 .4 1 1 0 1.3.2 2.5.6 3.6.1.3 0 .7-.2 1z"/>
    </svg>
    <span>555-310-2846</span><span class="divider">|</span><span>555-0192</span>
  </div>
</main>
</body>
</html>
```